Main Banner for Hullwrap.com, SIMPLE REDESIGN

We need to redesign the main banner that appears on the homepage of our website.

Attached in the project brief is a reference.

There are alot of things we like that we want to keep from that concept but its overall just something I drew on paint and not designed well.

1. Keep yellow tabs on the right hand side, we want them bigger and bolder and to showcase the bullet points inside.
2. Get rid of the 10 yr warranty emblem and replace that with our Brandell logo also attached to the brief.
3. Keep the bottom header and include hullwrap.com and the phone number, but make it look bolder and nicer.
4. Keep the watermark

Aside from these points what we really need is this but a better cleaner more professional version of it.

Target Market(s)

Visitors to our website hullwrap.com we want this banner to include all the major selling points, branding of the product and info on how to contact us.

Requirements
Must have
• Must be clean and professional. My fear is getting submissions that are too busy or messy. There are a lot of components but the challenge is to put them all in there in a clean professional way.
Should not have
• An image in the background like a beach or some kind of picture want the focus to be the requirements listed in the project description

```html
<!DOCTYPE html>
<html lang="en">
<head>
<meta charset="utf-8">
<title>Hullwrap.com Homepage Banner</title>
<link href="https://fonts.googleapis.com/css2?family=Open+Sans:ital,wght@0,300;0,400;0,700;0,800;1,300;1,400;1,700;1,800&display=swap" rel="stylesheet">
<style>
  :root {
    --stage: #e4e2df;
    --panel: #f7f7f7;
    --panel-edge: #e6e6e6;
    --ink: #2b2b2b;
    --ink-soft: #4a4a4a;
    --yellow-top: #ffe23a;
    --yellow-bottom: #f7b500;
    --yellow-deep: #e79d00;
    --star: #ffc400;
    --badge: #3d3d3d;
    --cover-blue: #2d3f8f;
    --hull-grey: #c9ccd2;
  }
  * { box-sizing: border-box; margin: 0; padding: 0; }
  html, body { width: 1159px; height: 1200px; overflow: hidden; }
  body {
    background: var(--stage);
    font-family: "Open Sans", Arial, sans-serif;
    color: var(--ink);
    position: relative;
  }
  .banner {
    position: absolute;
    left: 60px;
    width: 1020px;
    height: 500px;
    background: radial-gradient(ellipse at 55% 45%, #ffffff 0%, var(--panel) 55%, var(--panel-edge) 100%);
    box-shadow: 0 6px 18px rgba(0,0,0,.35);
    overflow: hidden;
  }
  .banner--one { top: 34px; }
  .banner--two { top: 620px; }

  .brand-badge {
    position: absolute; left: 18px; top: 18px;
    width: 88px; height: 88px;
    background: var(--badge);
    border-radius: 6px;
    display: flex; align-items: center; justify-content: center;
    font-weight: 700; font-size: 14px; letter-spacing: .5px;
    color: #ffffff;
  }
  .headline {
    position: absolute; left: 116px; top: 18px;
    font-size: 37px; font-weight: 300; text-transform: uppercase;
    letter-spacing: .3px; white-space: nowrap; line-height: 1.1;
    color: var(--ink-soft);
  }
  .headline strong { font-weight: 800; font-style: italic; color: var(--ink); }
  .price-row {
    position: absolute; left: 116px; top: 68px;
    display: flex; align-items: center; gap: 14px;
    font-size: 30px; font-weight: 300; text-transform: uppercase; color: var(--ink-soft);
    white-space: nowrap;
  }
  .price-row strong { font-weight: 700; font-style: italic; color: var(--ink); }
  .price-tag {
    font-size: 26px; font-weight: 800; font-style: italic; color: var(--ink);
    background: linear-gradient(var(--yellow-top), var(--yellow-bottom));
    padding: 4px 20px;
  }
  .banner--one .price-tag { clip-path: polygon(8% 0, 100% 0, 92% 100%, 0 100%); }
  .banner--two .price-tag { clip-path: polygon(8% 0, 92% 0, 100% 50%, 92% 100%, 8% 100%, 0 50%); padding: 4px 26px; }
  .stars { display: flex; gap: 4px; }
  .stars svg { width: 34px; height: 34px; fill: var(--star); }

  .product-photo {
    position: absolute; left: 8px; top: 152px;
    width: 640px; height: 280px;
    border-radius: 40% 40% 30% 30%;
    background: linear-gradient(180deg, var(--cover-blue) 0%, var(--cover-blue) 40%, var(--hull-grey) 62%, #e3e5e8 100%);
    opacity: .9;
  }
  .banner--two .product-photo { left: 20px; top: 175px; width: 580px; height: 260px; }

  .perks { position: absolute; right: 0; top: 145px; list-style: none; }
  .perk {
    position: absolute; right: 0;
    height: 56px;
    display: flex; align-items: center; gap: 12px;
    padding-left: 44px;
    font-size: 24px; font-weight: 300; font-style: italic; text-transform: uppercase;
    color: var(--ink); white-space: nowrap;
    background: linear-gradient(var(--yellow-top), var(--yellow-bottom));
    box-shadow: inset 0 -3px 0 var(--yellow-deep);
  }
  .perk strong { font-weight: 800; }
  .perk svg { width: 24px; height: 24px; flex: none; }
  .perk:nth-child(1) { top: 0; width: 350px; }
  .perk:nth-child(2) { top: 79px; width: 285px; }
  .perk:nth-child(3) { top: 158px; width: 292px; }
  .banner--one .perk { clip-path: polygon(24px 0, 100% 0, 100% 100%, 0 100%); }
  .banner--two .perk { clip-path: polygon(26px 0, 100% 0, 100% 100%, 26px 100%, 0 50%); }
  .banner--two .perks { top: 175px; }
  .banner--two .perk:nth-child(1) { width: 360px; }
  .banner--two .perk:nth-child(2) { width: 318px; top: 75px; }
  .banner--two .perk:nth-child(3) { width: 290px; top: 150px; }

  .contact-bar {
    position: absolute; left: 0; right: 0; bottom: 0; height: 48px;
    display: flex; align-items: center; justify-content: space-between;
    padding: 0 30px;
    font-size: 20px; text-transform: uppercase; color: var(--ink);
    background: linear-gradient(var(--yellow-top), var(--yellow-bottom));
    white-space: nowrap;
  }
  .contact-item { display: flex; align-items: center; gap: 10px; font-weight: 400; }
  .contact-item strong { font-weight: 800; font-style: italic; }
  .contact-item svg { width: 20px; height: 20px; fill: var(--ink); }
  .banner--two .contact-bar { background: none; padding: 0; bottom: 12px; }
  .banner--two .contact-item {
    height: 46px; padding: 0 40px 0 28px;
    background: linear-gradient(var(--yellow-top), var(--yellow-bottom));
  }
  .banner--two .contact-item--web { clip-path: polygon(0 0, calc(100% - 22px) 0, 100% 50%, calc(100% - 22px) 100%, 0 100%); }
  .banner--two .contact-item--phone { padding: 0 28px 0 46px; clip-path: polygon(22px 0, 100% 0, 100% 100%, 22px 100%, 0 50%); }
</style>
</head>
<body>

<svg width="0" height="0" style="position:absolute" aria-hidden="true">
  <defs>
    <symbol id="star" viewBox="0 0 24 24"><polygon points="12,1 15,9 23.5,9 16.7,14.2 19.3,22.5 12,17.4 4.7,22.5 7.3,14.2 0.5,9 9,9"/></symbol>
    <symbol id="check-box" viewBox="0 0 24 24"><rect x="2" y="4" width="17" height="17" rx="2" fill="none" stroke="#2b2b2b" stroke-width="2.2"/><path d="M6 12 l4 4 l11 -12" fill="none" stroke="#2b2b2b" stroke-width="2.6" stroke-linecap="round"/></symbol>
    <symbol id="phone" viewBox="0 0 24 24"><path d="M6.6 10.8a15 15 0 0 0 6.6 6.6l2.2-2.2a1 1 0 0 1 1-.25 11.4 11.4 0 0 0 3.6.57 1 1 0 0 1 1 1V20a1 1 0 0 1-1 1A17 17 0 0 1 3 4a1 1 0 0 1 1-1h3.5a1 1 0 0 1 1 1c0 1.25.2 2.45.57 3.57a1 1 0 0 1-.25 1z"/></symbol>
    <symbol id="globe" viewBox="0 0 24 24"><circle cx="12" cy="12" r="10"/></symbol>
  </defs>
</svg>

<section class="banner banner--one">
  <div class="brand-badge">BRANDELL</div>
  <h1 class="headline">Brandell <strong>Meridian 1200 Boat Cover</strong></h1>
  <div class="price-row">
    <span>Starting <strong>Price</strong></span>
    <span class="price-tag">$239.99</span>
    <span class="stars"><svg><use href="#star"/></svg><svg><use href="#star"/></svg><svg><use href="#star"/></svg><svg><use href="#star"/></svg><svg><use href="#star"/></svg></span>
  </div>
  <div class="product-photo" role="img" aria-label="Boat on a twin-axle trailer wrapped in a blue fitted cover with black straps"></div>
  <ul class="perks">
    <li class="perk"><svg><use href="#check-box"/></svg><span>10 Yr <strong>Warrenty</strong></span></li>
    <li class="perk"><svg><use href="#check-box"/></svg><span>Free <strong>Shipping</strong></span></li>
    <li class="perk"><svg><use href="#check-box"/></svg><span>Water <strong>Proof</strong></span></li>
  </ul>
  <footer class="contact-bar">
    <span class="contact-item contact-item--web"><svg><use href="#globe"/></svg><span><strong>Hullwrap</strong>.com</span></span>
    <span class="contact-item contact-item--phone"><svg><use href="#phone"/></svg><span><strong>Call Us</strong> 800-555-0142</span></span>
  </footer>
</section>

<section class="banner banner--two">
  <div class="brand-badge">BRANDELL</div>
  <h1 class="headline">Brandell <strong>Meridian 1200 Boat Cover</strong></h1>
  <div class="price-row">
    <span>Starting <strong>Price</strong></span>
    <span class="price-tag">$239.99</span>
    <span class="stars"><svg><use href="#star"/></svg><svg><use href="#star"/></svg><svg><use href="#star"/></svg><svg><use href="#star"/></svg><svg><use href="#star"/></svg></span>
  </div>
  <div class="product-photo" role="img" aria-label="Boat on a twin-axle trailer wrapped in a blue fitted cover with black straps"></div>
  <ul class="perks">
    <li class="perk"><svg><use href="#check-box"/></svg><span>10 Yr <strong>Warrenty</strong></span></li>
    <li class="perk"><svg><use href="#check-box"/></svg><span>Free <strong>Shipping</strong></span></li>
    <li class="perk"><svg><use href="#check-box"/></svg><span>Water <strong>Proof</strong></span></li>
  </ul>
  <footer class="contact-bar">
    <span class="contact-item contact-item--web"><svg><use href="#globe"/></svg><span><strong>Hullwrap</strong>.com</span></span>
    <span class="contact-item contact-item--phone"><svg><use href="#phone"/></svg><span><strong>Call Us</strong> 800-555-0142</span></span>
  </footer>
</section>

</body>
</html>
```